Brixo Tidy Yard Website

We need a website design for this new company. I've attached the company logo. This company is in the construction industry that provides general labor, maintenance and cleaning for construction sites. We want a clean and simple website that can be easy to navigate.

Target Market(s)

Construction industry

Industry/Entity Type

Construction

Number of Pages Required

2 page

Font styles to use
Sans Serif

```html
<!DOCTYPE html>
<html lang="en">
<head>
<meta charset="utf-8">
<title>Brixo Tidy Yard</title>
<link rel="stylesheet" href="https://fonts.googleapis.com/css2?family=Open+Sans:wght@400;600;700&display=swap">
<style>
:root{
  --navy:#07075c;
  --orange:#ff5010;
  --lilac:#e4e2f4;
  --hero:#5e5b9c;
  --white:#ffffff;
  --text:#3a3a4a;
  --muted:#9a98c8;
}
*{margin:0;padding:0;box-sizing:border-box}
html,body{width:1200px;height:2778px;overflow:hidden}
body{font-family:"Open Sans",Arial,sans-serif;background:var(--white);color:var(--text);position:relative}
.abs{position:absolute}

/* header & hero */
.hero{left:0;top:0;width:1200px;height:615px;background:linear-gradient(180deg,#4a4788 0%,#6b68a8 55%,#55528f 100%)}
.brand{left:144px;top:0;width:167px;height:107px;background:var(--white);display:flex;align-items:center;justify-content:center;text-align:center;color:var(--navy);font-weight:700;font-size:21px;line-height:1.1}
.nav{top:20px;left:333px;display:flex;font-size:17px;font-weight:600;color:var(--white)}
.nav a{color:inherit;text-decoration:none;position:absolute;white-space:nowrap}
.nav a.active{color:var(--orange)}
.phone{left:895px;top:14px;color:var(--white);font-size:25px;display:flex;align-items:center;gap:8px}
.hero-title{left:0;width:1200px;top:262px;text-align:center;color:var(--white);font-weight:700;font-size:33px;line-height:43px;letter-spacing:.3px}
.btn-orange{left:520px;top:359px;width:160px;height:41px;background:var(--orange);color:var(--white);font-weight:700;font-size:19px;display:flex;align-items:center;justify-content:center}
.arrow{top:292px}

/* headings */
.section-title{left:0;width:1200px;text-align:center;color:var(--navy);font-weight:700;font-size:32px}
.rule{left:528px;width:144px;height:5px;background:var(--orange)}
.intro{left:157px;top:766px;width:886px;text-align:center;font-size:14.5px;line-height:26px;color:#333}

/* service cards */
.card{top:887px;width:297px;height:491px;background:var(--navy);color:var(--white);text-align:center}
.card .photo{position:absolute;left:0;top:0;width:297px;height:200px}
.card .badge{position:absolute;left:100px;top:152px;width:96px;height:96px;border-radius:50%;background:var(--orange);display:flex;align-items:center;justify-content:center}
.card h3{position:absolute;left:0;width:297px;top:267px;font-size:20px;font-weight:700;line-height:29px}
.card p{position:absolute;left:24px;width:249px;top:330px;font-size:12px;line-height:20px;color:var(--muted)}
.card .more{position:absolute;left:93px;top:409px;width:111px;height:41px;border:1.5px solid var(--muted);color:#c8c6ea;font-size:13px;font-weight:600;display:flex;align-items:center;justify-content:center}

/* gallery */
.gallery-band{left:0;top:1457px;width:1200px;height:701px;background:var(--lilac)}
.tile{position:absolute}
.play{left:576px;top:1783px;width:48px;height:48px;border-radius:50%;background:var(--white)}
.btn-outline{left:544px;top:2033px;width:112px;height:43px;border:1.5px solid var(--navy);color:var(--navy);font-size:13px;font-weight:600;display:flex;align-items:center;justify-content:center}

/* contact */
.map{left:144px;top:2320px;width:454px;height:280px;background:linear-gradient(135deg,#d9dbdc,#c9d8b8 55%,#dadada)}
.info{left:598px;top:2320px;width:458px;height:280px;background:var(--lilac)}
.info-row{position:absolute;left:56px;display:flex;align-items:center;gap:12px;font-size:16px;color:var(--navy)}
.info-row svg{width:14px;height:14px;flex:none}

/* footer */
.footer{left:0;top:2682px;width:1200px;height:96px;background:var(--navy);color:var(--white)}
.footer-links{position:absolute;left:144px;top:23px;font-size:11px}
.footer-links span{margin:0 8px}
.copyright{position:absolute;left:144px;top:53px;font-size:11px}
.social{position:absolute;top:38px;width:14px;height:14px;background:#c8c6ea;border-radius:2px}
</style>
</head>
<body>

<header>
  <div class="abs hero" role="img" aria-label="Photo of construction workers in hard hats and safety vests facing scaffolding, with a purple tint"></div>
  <div class="abs brand">Brixo<br>Tidy Yard</div>
  <nav class="abs nav">
    <a class="active" style="left:0">HOME</a>
    <a style="left:89px">ABOUT US</a>
    <a style="left:211px">SERVICES</a>
    <a style="left:324px">GALLERY</a>
    <a style="left:434px">CONTACT US</a>
  </nav>
  <div class="abs phone">
    <svg width="18" height="18" viewBox="0 0 24 24"><path fill="#fff" d="M6.6 10.8a15.1 15.1 0 0 0 6.6 6.6l2.2-2.2a1 1 0 0 1 1-.25 11.4 11.4 0 0 0 3.6.57 1 1 0 0 1 1 1V20a1 1 0 0 1-1 1A17 17 0 0 1 3 4a1 1 0 0 1 1-1h3.5a1 1 0 0 1 1 1c0 1.25.2 2.45.57 3.57a1 1 0 0 1-.25 1z"/></svg>
    555 014 2291
  </div>
  <svg class="abs arrow" style="left:55px" width="24" height="30" viewBox="0 0 24 30"><path d="M18 3 6 15l12 12" fill="none" stroke="#fff" stroke-width="5"/></svg>
  <svg class="abs arrow" style="left:1120px" width="24" height="30" viewBox="0 0 24 30"><path d="M6 3l12 12L6 27" fill="none" stroke="#fff" stroke-width="5"/></svg>
  <h1 class="abs hero-title">MAECENAS TORTOR ACCUMSAN<br>QUAM VARIUS IMPERDIET</h1>
  <div class="abs btn-orange">CONTACT US</div>
</header>

<main>
  <h2 class="abs section-title" style="top:683px">WELCOME TO BRIXO TIDY YARD</h2>
  <div class="abs rule" style="top:741px"></div>
  <p class="abs intro">Vivamus efficitur ex condimentum, malesuada eros eget, feugiat nibh. Sed tellus ex, imperdiet eget gravida sit amet, volutpat eget turpis. In nec ultricies est. Etiam mattis augue vehicula odio posuere, sit amet tempus lectus luctus. Nulla facilisi. Etiam vel massa ele mentum, bibendum tellus venenatis, feugiat massa. Curabitur venenatis lacinia ornare.</p>

  <article class="abs card" style="left:144px">
    <div class="photo" role="img" aria-label="Photo of site supervisors in hard hats reviewing plans" style="background:linear-gradient(160deg,#8a7f70,#c9c3a0 60%,#d8d24a)"></div>
    <div class="badge"><svg width="48" height="48" viewBox="0 0 48 48" fill="none" stroke="#fff" stroke-width="2.5"><path d="M10 24a14 14 0 0 1 28 0"/><path d="M6 24h36"/><path d="M24 10v8"/><path d="M12 44v-6a12 8 0 0 1 24 0v6"/></svg></div>
    <h3>GENERAL LABOR</h3>
    <p>Quisque aliquet ex nec est vestibulum pulvinar. Pellentesque convallis molestie enim sit amet efficitur. Etiam id imperdiet lectus.</p>
    <div class="more">READ MORE</div>
  </article>

  <article class="abs card" style="left:452px">
    <div class="photo" role="img" aria-label="Photo of ironworkers on steel beams against a blue sky" style="background:linear-gradient(180deg,#4f7fc4,#a9c4e6 60%,#5a4e44)"></div>
    <div class="badge"><svg width="48" height="48" viewBox="0 0 48 48" fill="none" stroke="#fff" stroke-width="2.5"><path d="M14 8v10l-4 4v18h8V22l-4-4"/><path d="M32 6a6 6 0 0 0 0 12v24h6V18a6 6 0 0 0 0-12v6h-6z"/></svg></div>
    <h3>MAINTENANCE</h3>
    <p>Quisque aliquet ex nec est vestibulum pulvinar. Pellentesque convallis molestie enim sit amet efficitur. Etiam id imperdiet lectus.</p>
    <div class="more">READ MORE</div>
  </article>

  <article class="abs card" style="left:759px">
    <div class="photo" role="img" aria-label="Photo of a worker in a high-visibility vest cleaning a concrete site" style="background:linear-gradient(150deg,#7b7c7c,#b4b3ae 60%,#8f8e8a)"></div>
    <div class="badge"><svg width="48" height="48" viewBox="0 0 48 48" fill="none" stroke="#fff" stroke-width="2.5"><rect x="4" y="12" width="26" height="20"/><path d="M30 18h8l6 7v7H30z"/><circle cx="13" cy="35" r="4"/><circle cx="36" cy="35" r="4"/></svg></div>
    <h3>CONSTRUCTION SITES<br>CLEANING</h3>
    <p>Quisque aliquet ex nec est vestibulum pulvinar. Pellentesque convallis molestie enim sit amet efficitur. Etiam id imperdiet lectus.</p>
    <div class="more">READ MORE</div>
  </article>

  <section>
    <div class="abs gallery-band"></div>
    <h2 class="abs section-title" style="top:1526px">GALLERY</h2>
    <div class="abs rule" style="top:1584px"></div>
    <div class="tile" role="img" aria-label="Photo of an excavated pit marked with safety cones" style="left:144px;top:1615px;width:219px;height:185px;background:linear-gradient(160deg,#d7d3cf,#a59c92)"></div>
    <div class="tile" role="img" aria-label="Photo of a building under construction with cranes" style="left:144px;top:1815px;width:219px;height:185px;background:linear-gradient(180deg,#3f86d6,#9cc0e6 55%,#8f7f6e)"></div>
    <div class="tile" role="img" aria-label="Video still of workers in orange vests fitting ceiling ducts" style="left:374px;top:1615px;width:452px;height:385px;background:linear-gradient(135deg,#b9bcc0,#8a8f94 50%,#d0763a)"></div>
    <div class="tile" role="img" aria-label="Photo of workers in yellow vests with a wheelbarrow" style="left:839px;top:1615px;width:217px;height:185px;background:linear-gradient(170deg,#c8c2b5,#d8d0bc 60%,#a33b34)"></div>
    <div class="tile" role="img" aria-label="Photo of two builders in hard hats laying rebar" style="left:839px;top:1815px;width:217px;height:185px;background:linear-gradient(160deg,#9e7a55,#6c7f96 60%,#7a5a3c)"></div>
    <div class="abs play"></div>
    <svg class="abs" style="left:593px;top:1797px" width="18" height="20" viewBox="0 0 18 20"><path d="M2 1l15 9-15 9z" fill="#333"/></svg>
    <div class="abs btn-outline">READ MORE</div>
  </section>

  <section>
    <h2 class="abs section-title" style="top:2224px">CONTACT US</h2>
    <div class="abs rule" style="top:2284px"></div>
    <div class="abs map" role="img" aria-label="City street map showing the office location"></div>
    <div class="abs info">
      <div class="info-row" style="top:56px"><svg viewBox="0 0 24 24"><path fill="#07075c" d="M12 2a7 7 0 0 0-7 7c0 5 7 13 7 13s7-8 7-13a7 7 0 0 0-7-7zm0 9.5A2.5 2.5 0 1 1 12 6.5a2.5 2.5 0 0 1 0 5z"/></svg>18 Quarry Lane, Mill Street, Eastford 40215</div>
      <div class="info-row" style="top:104px"><svg viewBox="0 0 24 24"><path fill="#07075c" d="M6.6 10.8a15.1 15.1 0 0 0 6.6 6.6l2.2-2.2a1 1 0 0 1 1-.25 11.4 11.4 0 0 0 3.6.57 1 1 0 0 1 1 1V20a1 1 0 0 1-1 1A17 17 0 0 1 3 4a1 1 0 0 1 1-1h3.5a1 1 0 0 1 1 1c0 1.25.2 2.45.57 3.57a1 1 0 0 1-.25 1z"/></svg>Phone : 555 014 2290</div>
      <div class="info-row" style="top:152px"><svg viewBox="0 0 24 24"><path fill="#07075c" d="M6 2h9v5H6zM3 8h18v11H3zm3 3v2h4v-2zm0 4v2h4v-2zm7-4v6h5v-6z"/></svg>Fax : 555 014 2299</div>
      <div class="info-row" style="top:200px"><svg viewBox="0 0 24 24"><path fill="#07075c" d="M2 5h20v14H2zm2 2v.5l8 5 8-5V7z"/></svg>Email : hello@brixotidyyard.com</div>
    </div>
  </section>
</main>

<footer class="abs footer">
  <div class="footer-links">Home<span>|</span>About Us<span>|</span>Services<span>|</span>Gallery<span>|</span>Contact Us</div>
  <div class="copyright">Copyright &copy; 2019&nbsp; Brixo Tidy Yard.&nbsp; All rights reserved.</div>
  <div class="social" style="left:1003px"></div>
  <div class="social" style="left:1039px"></div>
</footer>

</body>
</html>
```